Falcrest security business card

Looking for a business card for my security company

Target Market(s)

Security

Industry/Entity Type

Security

Contact Information for Business Card

Name - Gil Marston. Title - General manager - direct 314 862.4490 website www. falcrestsecurityservices.example email - gil@ falcrestsecurityservices.example

Requirements
Must have
• Logo attached

```html
<!DOCTYPE html>
<html lang="en">
<head>
<meta charset="utf-8">
<title>Falcrest Security Business Card</title>
<link rel="stylesheet" href="https://fonts.googleapis.com/css2?family=Montserrat:wght@600&family=Roboto:wght@400&display=swap">
<style>
  :root {
    --backdrop: #222222;
    --card: #161616;
    --gold: #c9a45a;
    --gold-soft: #a8853f;
  }
  * { margin: 0; padding: 0; box-sizing: border-box; }
  html, body {
    width: 1200px;
    height: 900px;
    overflow: hidden;
    background: var(--backdrop);
  }
  .sheet {
    position: relative;
    width: 1200px;
    height: 900px;
  }
  .card {
    position: absolute;
    left: 250px;
    width: 700px;
    height: 400px;
    background: var(--card);
    border: 1.5px solid var(--gold-soft);
    border-radius: 18px;
    overflow: hidden;
  }
  .card--front { top: 35px; }
  .card--back { top: 465px; }

  .wordmark {
    display: flex;
    align-items: center;
    gap: 14px;
    font-family: "Montserrat", sans-serif;
    font-weight: 600;
    color: var(--gold);
    letter-spacing: 0.04em;
    text-transform: uppercase;
  }
  .wordmark__square {
    background: var(--gold);
    flex: none;
  }
  .card--front .wordmark {
    position: absolute;
    left: 50%;
    top: 50%;
    transform: translate(-50%, -50%);
    font-size: 64px;
  }
  .card--front .wordmark__square { width: 40px; height: 40px; }

  .card--back .wordmark {
    position: absolute;
    left: 200px;
    top: 56px;
    font-size: 42px;
  }
  .card--back .wordmark__square { width: 26px; height: 26px; }

  .divider {
    position: absolute;
    left: 60px;
    top: 190px;
    width: 390px;
    height: 1px;
    background: var(--gold);
  }
  .contact {
    position: absolute;
    left: 40px;
    top: 232px;
    list-style: none;
    font-family: "Roboto", sans-serif;
    font-size: 15px;
    line-height: 24px;
    color: var(--gold);
  }
  .contact li { display: flex; align-items: center; gap: 8px; }
  .contact svg { width: 12px; height: 12px; flex: none; }

  .person {
    position: absolute;
    right: 60px;
    top: 196px;
    text-align: left;
  }
  .person__name {
    font-family: "Montserrat", sans-serif;
    font-weight: 600;
    font-size: 34px;
    letter-spacing: 0.06em;
    color: var(--gold);
    text-transform: uppercase;
    line-height: 1.1;
  }
  .person__title {
    font-family: "Roboto", sans-serif;
    font-size: 20px;
    color: var(--gold);
    padding-left: 120px;
    letter-spacing: 0.02em;
  }
  .edge-tab {
    position: absolute;
    right: 0;
    top: 300px;
    width: 8px;
    height: 44px;
    background: var(--gold);
  }
</style>
</head>
<body>
<main class="sheet">
  <section class="card card--front" aria-label="Card front">
    <div class="wordmark"><span class="wordmark__square"></span>Falcrest</div>
  </section>

  <section class="card card--back" aria-label="Card back">
    <div class="wordmark"><span class="wordmark__square"></span>Falcrest</div>
    <div class="divider"></div>
    <ul class="contact">
      <li>
        <svg viewBox="0 0 12 12" aria-hidden="true"><path d="M2.5 1l2 2.2-1 1.3c.7 1.5 1.8 2.6 3.3 3.3l1.3-1 2.2 2-1.2 1.7C5 10.2 1.8 7 .8 2.2z" fill="var(--gold)"/></svg>
        314 862.4490
      </li>
      <li>
        <svg viewBox="0 0 12 12" aria-hidden="true"><rect x="0.5" y="2.5" width="11" height="7" fill="none" stroke="var(--gold)"/><path d="M0.5 2.5L6 6.5l5.5-4" fill="none" stroke="var(--gold)"/></svg>
        gil@ falcrestsecurityservices.example
      </li>
      <li>
        <svg viewBox="0 0 12 12" aria-hidden="true"><circle cx="6" cy="6" r="5.3" fill="none" stroke="var(--gold)"/><ellipse cx="6" cy="6" rx="2.2" ry="5.3" fill="none" stroke="var(--gold)"/><path d="M.7 6h10.6" stroke="var(--gold)"/></svg>
        www. falcrestsecurityservices.example
      </li>
    </ul>
    <div class="person">
      <div class="person__name">Gil Marston</div>
      <div class="person__title">General manager</div>
    </div>
    <div class="edge-tab"></div>
  </section>
</main>
</body>
</html>
```